International Petrochemical business needs a web design for Tessaro Desk system

We need a web design for a "Tessaro Desk" system for an international petrochemical company. The web site is used internally within the company. It is hosted by an internal department which provides government permit request service for other departments.

We would like to see designs of two pages using color light blue. (home page, internal page as attached).
Home Page:
1. Header has a background image and small animation. Header on home page can be taller than the header of the internal page.
2. Layout as attached.

Internal Page:
1. Header can use the same background image as the home page and can be shorter to utilize the page for content.
2. The blue icon behind every captions represent an icon. When user move mouse over this icon, it displays the caption in Thai language as a tooltip. This icon needs to be redesign.

The final design should communicate the followings:
- Excellent service provided system in terms of time and accurary
- Rapid growth of business via building petrochemical refinery plant

For Internal Page, the blue circle behind every captions represent an icon. When mouse over this icon, a tool tip showing the caption in Thai language is shown. Please also design this icon..

There are more feedbacks from customer as followed:

1. Banner should consists of 
    1.1 "Approved" stamp on paper
    1.2 An image of Garuda. It is used on every government documents in Thailand
    1.3 Image of petrochemical plant
2. Each menu item (Home, Permit, Search, etc) should have different colors. Drop down menu will use the same color as its parent menu item.
3. Overall tone of the web page should be light blue with background of the body the web page in white
4. "New Request" button should use green color with icon on it
5. Table header of each box in the body of the page should use dark blue background with text in white

Please kindly submit your revisions.
Thank you.

Reason: We get some late feedbacks from customers which was just updated to all designers.

• 1. Design for 1024x768 screen resolution
2. Use light blue theme
3. Background of header where the company logo is must have white background

```html
<!DOCTYPE html>
<html lang="en">
<head>
<meta charset="utf-8">
<title>Tessaro Desk – Home</title>
<link rel="stylesheet" href="https://fonts.googleapis.com/css2?family=Yanone+Kaffeesatz:wght@300;400&family=Open+Sans:wght@500;600&family=Mulish:wght@400;500&display=swap">
<style>
:root{
  --sky:#1ab3ea;
  --sky-dark:#0f9fd6;
  --navy:#2b2a6e;
  --grey-bar:#8c8c8c;
  --panel:#f7f7f7;
  --panel-line:#e6e6e6;
  --text:#333333;
  --muted:#8a8a8a;
  --btn:#d9d9d9;
  --btn-icon:#6f6f6f;
  --white:#ffffff;
}
*{margin:0;padding:0;box-sizing:border-box}
html,body{width:1200px;height:627px;overflow:hidden;background:var(--white)}
body{position:relative;font-family:"Mulish",sans-serif;color:var(--text)}

.backdrop{position:absolute;inset:0;height:520px;
  background:linear-gradient(180deg,#eeeeee 0%,#e3e3e3 45%,#efefef 80%,#ffffff 100%)}

.brand{position:absolute;left:198px;top:14px;display:flex;align-items:center;gap:8px}
.brand-dot{width:32px;height:32px;border-radius:50%;background:var(--sky)}
.brand-name{font-family:"Open Sans",sans-serif;font-weight:600;font-size:15px;line-height:17px;color:var(--navy);width:130px}

.main-nav{position:absolute;top:24px;left:560px;height:26px;font-family:"Yanone Kaffeesatz",sans-serif;font-weight:400;font-size:21px;color:#555}
.nav-item{position:absolute;top:0;height:26px;line-height:27px;white-space:nowrap}
.nav-item.is-active{background:var(--sky);color:var(--white);width:64px;text-align:center}
.nav-sep{position:absolute;top:4px;height:20px;border-left:1px dotted #999}
.nav-caret{display:inline-block;margin-left:8px;vertical-align:2px}

.panel{position:absolute;background:var(--panel);border:1px solid #eeeeee}
.panel-title{height:22px;line-height:22px;padding-left:18px;font-family:"Open Sans",sans-serif;font-weight:500;font-size:13.5px;color:var(--white);
  background-color:var(--sky);background-image:radial-gradient(rgba(255,255,255,.12) 1px,transparent 1px);background-size:3px 3px}
.panel-title.is-grey{background-color:var(--grey-bar)}

.cell{position:absolute;white-space:nowrap}
.col-head{font-family:"Open Sans",sans-serif;font-weight:500;font-size:12.5px;color:var(--sky)}
.col-val{font-size:10.5px;color:#222}
.num{text-align:right}

.scroll-track{position:absolute;top:28px;bottom:8px;border-left:1px dotted #777}
.scroll-thumb{position:absolute;width:6px;height:34px;border-radius:2px;background:#777;margin-left:-3px}

.pager{position:absolute;left:0;right:0;display:flex;justify-content:center;align-items:center;font-size:11px;color:var(--muted)}
.pg-btn{width:23px;height:21px;border-radius:3px;background:var(--btn);display:flex;align-items:center;justify-content:center}
.pg-first{margin-right:29px}
.pg-last{margin-left:42px}
.pg-label{margin:0 6px 0 7px}
.pg-input{width:23px;height:14px;border:1px solid #aaa;background:var(--white);font-size:9px;line-height:12px;color:#999;text-align:center;margin-right:7px}
.pg-of{margin-right:11px}

.footer-bar{position:absolute;left:0;right:0;bottom:0;height:37px;background:#f1f1f1}

.new-request-btn{position:absolute;left:727px;top:385px;width:287px;height:39px;background:var(--sky);color:var(--white);
  font-family:"Yanone Kaffeesatz",sans-serif;font-size:28px;line-height:40px;text-align:center;letter-spacing:.5px}

.site-footer{position:absolute;left:186px;top:577px;font-family:"Open Sans",sans-serif;font-size:10px;color:#444}
.social{position:absolute;top:570px;left:912px;display:flex;gap:7px}
.social span{width:20px;height:20px;border-radius:3px;background:#c9c9c9}
</style>
</head>
<body>
<div class="backdrop" role="img" aria-label="Faint grey photo of a petrochemical refinery plant with pumpjacks and towers"></div>

<header>
  <div class="brand"><span class="brand-dot"></span><span class="brand-name">NORVALE PETROCHEMICAL</span></div>
  <nav class="main-nav">
    <span class="nav-item is-active" style="left:0">HOME</span>
    <span class="nav-item" style="left:80px">PERMITS<svg class="nav-caret" width="12" height="8" viewBox="0 0 12 8"><path d="M0 0H12L6 8Z" fill="#555"/></svg></span>
    <span class="nav-sep" style="left:169px"></span>
    <span class="nav-item" style="left:177px">SEARCH</span>
    <span class="nav-sep" style="left:242px"></span>
    <span class="nav-item" style="left:254px">REPORT</span>
    <span class="nav-sep" style="left:322px"></span>
    <span class="nav-item" style="left:336px">ADMIN</span>
    <span class="nav-sep" style="left:396px"></span>
    <span class="nav-item" style="left:412px">HELP</span>
  </nav>
</header>

<main>
  <!-- New Request -->
  <section class="panel" style="left:182px;top:71px;width:409px;height:147px">
    <h2 class="panel-title">New Request</h2>
    <span class="cell col-head" style="left:18px;top:29px">Request No.</span>
    <span class="cell col-head" style="left:111px;top:29px">Request Date</span>
    <span class="cell col-head" style="left:218px;top:29px">Branch</span>
    <span class="cell col-val" style="left:18px;top:51px">56-0003</span><span class="cell col-val" style="left:111px;top:51px">20/4/2013</span><span class="cell col-val" style="left:218px;top:51px">GC1</span>
    <span class="cell col-val" style="left:18px;top:69px">56-0003</span><span class="cell col-val" style="left:111px;top:69px">21/4/2013</span><span class="cell col-val" style="left:218px;top:69px">GC2</span>
    <span class="cell col-val" style="left:18px;top:87px">56-0003</span><span class="cell col-val" style="left:111px;top:87px">22/4/2013</span><span class="cell col-val" style="left:218px;top:87px">GC3</span>
    <div class="scroll-track" style="left:399px"><span class="scroll-thumb" style="top:14px"></span></div>
    <div class="pager" style="top:121px">
      <span class="pg-btn pg-first"><svg width="14" height="12" viewBox="0 0 14 12"><path d="M7 1 2 6l5 5M12 1 7 6l5 5" fill="none" stroke="#6f6f6f" stroke-width="2"/></svg></span>
      <span class="pg-btn"><svg width="8" height="12" viewBox="0 0 8 12"><path d="M6 1 1 6l5 5" fill="none" stroke="#6f6f6f" stroke-width="2"/></svg></span>
      <span class="pg-label">Page</span><span class="pg-input">1</span><span class="pg-of">of 1</span>
      <span class="pg-btn"><svg width="8" height="12" viewBox="0 0 8 12"><path d="M2 1l5 5-5 5" fill="none" stroke="#6f6f6f" stroke-width="2"/></svg></span>
      <span class="pg-btn pg-last"><svg width="14" height="12" viewBox="0 0 14 12"><path d="M2 1l5 5-5 5M7 1l5 5-5 5" fill="none" stroke="#6f6f6f" stroke-width="2"/></svg></span>
    </div>
  </section>

  <!-- My Working Request -->
  <section class="panel" style="left:605px;top:71px;width:409px;height:147px">
    <h2 class="panel-title is-grey">My Working Request</h2>
    <span class="cell col-head" style="left:18px;top:29px">Request No.</span>
    <span class="cell col-head" style="left:111px;top:29px">Request Date</span>
    <span class="cell col-head" style="left:218px;top:29px">Branch</span>
    <span class="cell col-val" style="left:18px;top:51px">56-0003</span><span class="cell col-val" style="left:111px;top:51px">20/4/2013</span><span class="cell col-val" style="left:218px;top:51px">waiting for process</span>
    <span class="cell col-val" style="left:18px;top:69px">56-0003</span><span class="cell col-val" style="left:111px;top:69px">21/4/2013</span><span class="cell col-val" style="left:218px;top:69px">In Progress</span>
    <span class="cell col-val" style="left:18px;top:87px">56-0003</span><span class="cell col-val" style="left:111px;top:87px">22/4/2013</span><span class="cell col-val" style="left:218px;top:87px">in complete document</span>
    <div class="scroll-track" style="left:399px"><span class="scroll-thumb" style="top:14px"></span></div>
    <div class="pager" style="top:121px">
      <span class="pg-btn pg-first"><svg width="14" height="12" viewBox="0 0 14 12"><path d="M7 1 2 6l5 5M12 1 7 6l5 5" fill="none" stroke="#6f6f6f" stroke-width="2"/></svg></span>
      <span class="pg-btn"><svg width="8" height="12" viewBox="0 0 8 12"><path d="M6 1 1 6l5 5" fill="none" stroke="#6f6f6f" stroke-width="2"/></svg></span>
      <span class="pg-label">Page</span><span class="pg-input">1</span><span class="pg-of">of 1</span>
      <span class="pg-btn"><svg width="8" height="12" viewBox="0 0 8 12"><path d="M2 1l5 5-5 5" fill="none" stroke="#6f6f6f" stroke-width="2"/></svg></span>
      <span class="pg-btn pg-last"><svg width="14" height="12" viewBox="0 0 14 12"><path d="M2 1l5 5-5 5M7 1l5 5-5 5" fill="none" stroke="#6f6f6f" stroke-width="2"/></svg></span>
    </div>
  </section>

  <!-- Expiring Permits -->
  <section class="panel" style="left:182px;top:227px;width:832px;height:147px">
    <h2 class="panel-title">Expiring Permits</h2>
    <span class="cell col-head" style="left:18px;top:29px">Permit No.</span>
    <span class="cell col-head" style="left:111px;top:29px">Expire Date</span>
    <span class="cell col-head" style="left:381px;top:29px">Branch</span>
    <span class="cell col-head" style="left:559px;top:29px">Required Time (Day)</span>
    <span class="cell col-head" style="left:725px;top:29px">Due Dated</span>
    <span class="cell col-val" style="left:18px;top:51px">56-0003</span><span class="cell col-val" style="left:111px;top:51px">20/4/2013</span><span class="cell col-val" style="left:381px;top:51px">GC1</span><span class="cell col-val num" style="right:159px;top:51px">30</span><span class="cell col-val num" style="right:45px;top:51px">-40</span>
    <span class="cell col-val" style="left:18px;top:69px">56-0003</span><span class="cell col-val" style="left:111px;top:69px">21/4/2013</span><span class="cell col-val" style="left:381px;top:69px">GC2</span><span class="cell col-val num" style="right:159px;top:69px">60</span><span class="cell col-val num" style="right:45px;top:69px">15</span>
    <span class="cell col-val" style="left:18px;top:87px">56-0003</span><span class="cell col-val" style="left:111px;top:87px">22/4/2013</span><span class="cell col-val" style="left:381px;top:87px">GC3</span><span class="cell col-val num" style="right:159px;top:87px">50</span><span class="cell col-val num" style="right:45px;top:87px">25</span>
    <div class="scroll-track" style="left:822px"><span class="scroll-thumb" style="top:14px"></span></div>
    <div class="pager" style="top:116px">
      <span class="pg-btn pg-first"><svg width="14" height="12" viewBox="0 0 14 12"><path d="M7 1 2 6l5 5M12 1 7 6l5 5" fill="none" stroke="#6f6f6f" stroke-width="2"/></svg></span>
      <span class="pg-btn"><svg width="8" height="12" viewBox="0 0 8 12"><path d="M6 1 1 6l5 5" fill="none" stroke="#6f6f6f" stroke-width="2"/></svg></span>
      <span class="pg-label">Page</span><span class="pg-input">1</span><span class="pg-of">of 1</span>
      <span class="pg-btn"><svg width="8" height="12" viewBox="0 0 8 12"><path d="M2 1l5 5-5 5" fill="none" stroke="#6f6f6f" stroke-width="2"/></svg></span>
      <span class="pg-btn pg-last"><svg width="14" height="12" viewBox="0 0 14 12"><path d="M2 1l5 5-5 5M7 1l5 5-5 5" fill="none" stroke="#6f6f6f" stroke-width="2"/></svg></span>
    </div>
  </section>

  <!-- My In Progress Requests -->
  <section class="panel" style="left:182px;top:385px;width:537px;height:173px;background:var(--white)">
    <h2 class="panel-title is-grey">My In Progress Requests</h2>
    <span class="cell col-head" style="left:18px;top:32px">Request No.</span>
    <span class="cell col-head" style="left:144px;top:32px">Requested</span>
    <span class="cell col-head" style="left:270px;top:32px">Status</span>
    <span class="cell col-val" style="left:18px;top:54px">56-0003</span><span class="cell col-val" style="left:144px;top:54px">20/4/2013</span><span class="cell col-val" style="left:270px;top:54px">lorem ipsum dolor sit amtem dotem totun khabun</span>
    <span class="cell col-val" style="left:18px;top:77px">56-0003</span><span class="cell col-val" style="left:144px;top:77px">20/4/2013</span><span class="cell col-val" style="left:270px;top:77px">lorem ipsum dolor sit amtem dotem totun khabun</span>
    <div class="footer-bar"></div>
    <div class="pager" style="top:146px">
      <span class="pg-btn pg-first"><svg width="14" height="12" viewBox="0 0 14 12"><path d="M7 1 2 6l5 5M12 1 7 6l5 5" fill="none" stroke="#6f6f6f" stroke-width="2"/></svg></span>
      <span class="pg-btn"><svg width="8" height="12" viewBox="0 0 8 12"><path d="M6 1 1 6l5 5" fill="none" stroke="#6f6f6f" stroke-width="2"/></svg></span>
      <span class="pg-label">Page</span><span class="pg-input">1</span><span class="pg-of">of 1</span>
      <span class="pg-btn"><svg width="8" height="12" viewBox="0 0 8 12"><path d="M2 1l5 5-5 5" fill="none" stroke="#6f6f6f" stroke-width="2"/></svg></span>
      <span class="pg-btn pg-last"><svg width="14" height="12" viewBox="0 0 14 12"><path d="M2 1l5 5-5 5M7 1l5 5-5 5" fill="none" stroke="#6f6f6f" stroke-width="2"/></svg></span>
    </div>
  </section>

  <div class="new-request-btn">NEW REQUEST</div>

  <!-- Recent Completed Requests -->
  <section class="panel" style="left:727px;top:432px;width:287px;height:126px;background:var(--white)">
    <h2 class="panel-title is-grey">Recent Completed Requests</h2>
    <span class="cell col-head" style="left:14px;top:30px">Request No.</span>
    <span class="cell col-head" style="left:141px;top:30px">Completed Date</span>
    <span class="cell col-val" style="left:14px;top:52px">56-0003</span><span class="cell col-val" style="left:141px;top:52px">20/4/2013</span>
    <span class="cell col-val" style="left:14px;top:70px">56-0003</span><span class="cell col-val" style="left:141px;top:70px">21/4/2013</span>
    <div class="footer-bar" style="height:30px"></div>
    <div class="pager" style="top:96px">
      <span class="pg-btn pg-first"><svg width="14" height="12" viewBox="0 0 14 12"><path d="M7 1 2 6l5 5M12 1 7 6l5 5" fill="none" stroke="#6f6f6f" stroke-width="2"/></svg></span>
      <span class="pg-btn"><svg width="8" height="12" viewBox="0 0 8 12"><path d="M6 1 1 6l5 5" fill="none" stroke="#6f6f6f" stroke-width="2"/></svg></span>
      <span class="pg-label">Page</span><span class="pg-input">1</span><span class="pg-of">of 1</span>
      <span class="pg-btn"><svg width="8" height="12" viewBox="0 0 8 12"><path d="M2 1l5 5-5 5" fill="none" stroke="#6f6f6f" stroke-width="2"/></svg></span>
      <span class="pg-btn pg-last" style="margin-left:42px"><svg width="14" height="12" viewBox="0 0 14 12"><path d="M2 1l5 5-5 5M7 1l5 5-5 5" fill="none" stroke="#6f6f6f" stroke-width="2"/></svg></span>
    </div>
  </section>
</main>

<footer>
  <p class="site-footer">© 2013 | Norvale Petrochemicals. All rights reserved</p>
  <div class="social"><span></span><span></span><span></span><span></span></div>
</footer>
</body>
</html>
```